Redesign of a facility management homepage

We need a redesign/an improved design of the facility management homepage (http://www.kolvenhaus-drefling.de/).
This websites offers detailed information on the "About us" as company, the "Services" provided and special information on facility and strata management. We would like to keep the structure of the website.
We need ideas/designs how this website could look more modern and confidential and appealing/pleasant for visitors at the same time and not losing the main purpose of information distribution.
The green color must be used since this is the basic color from our logo.
The blue in the background of the logo ist optional. So feel to use it or not.
We need no coding only design (.psd or as .ai)
Industry/Entity Type
It Company
Look and feel
Each slider illustrates characteristics of the customer's brand and the style your logo design should communicate.

```html
<!DOCTYPE html>
<html lang="de">
<head>
<meta charset="utf-8">
<title>KHD Büro- und Hausmeisterservice GmbH Drefling</title>
<link href="https://fonts.googleapis.com/css2?family=Roboto:wght@300;400;500&display=swap" rel="stylesheet">
<style>
:root{
  --green:#2a8a25;
  --green-dark:#237a1f;
  --green-light:#8cc63f;
  --text:#444;
  --nav-bg:#f7f7f7;
  --line:#d9d9d9;
  --white:#fff;
}
*{margin:0;padding:0;box-sizing:border-box}
html,body{width:1200px;height:879px;overflow:hidden;background:var(--white);font-family:'Roboto',Arial,sans-serif;color:var(--text)}
.page{position:relative;width:1200px;height:879px}
.top-stripe{height:5px;background:repeating-linear-gradient(90deg,var(--green-light) 0 52px,var(--green) 52px 104px,var(--green-light) 104px 156px,var(--green-dark) 156px 208px)}
.header{height:87px;display:flex;align-items:center;padding:0 24px;background:linear-gradient(#fff,#f3f3f3)}
.brand{display:flex;align-items:center;gap:14px}
.brand-mark{width:20px;height:20px;background:var(--green)}
.brand-name{font-size:30px;font-weight:500;color:var(--green);letter-spacing:1px}
.brand-text{margin-left:14px}
.brand-title{font-size:22px;font-weight:300;color:var(--green)}
.brand-tag{font-size:16px;color:#222}
.call{margin-left:auto;display:flex;align-items:baseline;gap:8px}
.call-label{font-size:22px;color:#222;font-weight:300}
.call-number{font-size:36px;color:#5a9a2a;font-weight:300}
.nav{display:flex;height:45px;border-top:1px solid var(--line);border-bottom:1px solid var(--line);background:var(--nav-bg)}
.nav a{display:flex;align-items:center;justify-content:center;font-size:15px;color:#333;text-decoration:none;border-right:1px solid var(--line)}
.nav a:nth-child(1){width:166px}
.nav a:nth-child(2){width:163px}
.nav a:nth-child(3){width:246px}
.nav a:nth-child(4){width:231px}
.nav a:nth-child(5){width:182px}
.nav a:nth-child(6){flex:1;border-right:0}
.slider{position:relative;height:332px;display:flex}
.slide-side{width:252px;background:linear-gradient(135deg,#9a9a9a,#e8e8e8 40%,#777)}
.slide-side.right{width:251px;background:linear-gradient(135deg,#bbb,#555 50%,#999)}
.slide-main{width:697px;background:linear-gradient(180deg,#d8a25e 0%,#a98f6a 30%,#e6e8e6 55%,#6c6c66 100%)}
.arrow{position:absolute;top:147px;width:38px;height:38px;border-radius:50%;background:var(--white);box-shadow:0 1px 4px rgba(0,0,0,.4);display:flex;align-items:center;justify-content:center}
.arrow.prev{left:230px}.arrow.next{left:932px}
.caption{position:absolute;left:511px;top:240px;width:178px;height:31px;background:rgba(20,20,20,.85);color:#fff;font-size:17px;font-weight:300;display:flex;align-items:center;justify-content:center}
.features{display:flex;height:112px;border-bottom:1px solid var(--line)}
.feature{flex:1;display:flex;align-items:center;justify-content:space-between;padding:0 24px;background:linear-gradient(#fff,#eee);border-right:1px solid var(--line)}
.feature:last-child{border-right:0}
.feature-title{font-size:19px;color:var(--green);font-weight:300;line-height:1.2}
.feature-art{width:100px;height:90px;border-radius:8px}
.art-person{width:84px;background:radial-gradient(circle at 40% 40%,#f0c8a0,#3aa43a 70%)}
.art-contact{background:linear-gradient(135deg,#2a7fd0,#dfe8f0)}
.art-links{width:130px;background:linear-gradient(135deg,#d8dcd0,#606060)}
.art-imprint{width:140px;background:linear-gradient(135deg,#f0d0b8,#555 60%,#f0d0b8)}
.content{display:flex;height:249px;padding:30px 24px 0}
.welcome{width:430px}
.welcome h1{font-size:23px;font-weight:300;color:var(--green);margin-bottom:8px}
.welcome p{font-size:14px;line-height:19px;margin-bottom:6px}
.more{font-size:13px;font-weight:500;color:var(--green);text-decoration:none}
.van{width:372px;height:205px;margin:-10px 0 0 20px;border-radius:40px 60px 20px 20px;background:linear-gradient(180deg,#e9ecef,#fafafa 50%,#cfd3d6)}
.contact{margin-left:auto;width:290px;padding-top:6px}
.contact h2{font-size:15px;font-weight:500;color:var(--green);margin-bottom:8px}
.row{display:flex;gap:8px;font-size:13px;line-height:19px;color:#555;margin-bottom:5px}
.row svg{flex:none;margin-top:3px}
.footer{position:absolute;left:0;bottom:0;width:1200px;height:49px;background:var(--green-dark);color:#fff;display:flex;align-items:center;justify-content:space-between;padding:0 24px;font-size:14px;font-weight:500}
.footer a{color:#fff;text-decoration:none}
</style>
</head>
<body>
<div class="page">
  <div class="top-stripe"></div>
  <header class="header">
    <div class="brand">
      <span class="brand-mark"></span>
      <span class="brand-name">KHD</span>
    </div>
    <div class="brand-text">
      <div class="brand-title">Büro- und Hausmeisterservice GmbH Drefling</div>
      <div class="brand-tag">Ihr Partner vor Ort.</div>
    </div>
    <div class="call"><span class="call-label">Call Now:</span><span class="call-number">0 48 15/23 47 60</span></div>
  </header>
  <nav class="nav">
    <a href="#">Home</a><a href="#">About Us</a><a href="#">Gebaeudemanagement</a><a href="#">Gebaeudeverwaltung</a><a href="#">Vermietung</a><a href="#">Contact Us</a>
  </nav>
  <section class="slider">
    <div class="slide-side" role="img" aria-label="Photo of a white company van"></div>
    <div class="slide-main" role="img" aria-label="Photo of the company fleet of white vans parked in front of buildings"></div>
    <div class="slide-side right" role="img" aria-label="Black and white photo of a small utility vehicle"></div>
    <span class="arrow prev"><svg width="14" height="14" viewBox="0 0 14 14"><path d="M9 2 4 7l5 5" fill="none" stroke="#333" stroke-width="2.5"/></svg></span>
    <span class="arrow next"><svg width="14" height="14" viewBox="0 0 14 14"><path d="M5 2l5 5-5 5" fill="none" stroke="#333" stroke-width="2.5"/></svg></span>
    <div class="caption">OUR FLEET</div>
  </section>
  <section class="features">
    <div class="feature"><span class="feature-title">Storung online<br>melden</span><span class="feature-art art-person" role="img" aria-label="Illustration of a support person with info badge"></span></div>
    <div class="feature"><span class="feature-title">Kontakt</span><span class="feature-art art-contact" role="img" aria-label="Illustration of a telephone and an email envelope"></span></div>
    <div class="feature"><span class="feature-title">Links</span><span class="feature-art art-links" role="img" aria-label="Illustration of charts, banknotes and a calculator"></span></div>
    <div class="feature"><span class="feature-title">Impressum</span><span class="feature-art art-imprint" role="img" aria-label="Illustration of hands holding a small house"></span></div>
  </section>
  <section class="content">
    <div class="welcome">
      <h1>Welcome to Our Website:</h1>
      <p>Die K H D ist ein etabliertes, erfahrenes und erfolgreiches Dienstleistungsunternehmen mit den Sparten Gebäudemanagement (Gebäudeverwaltung, Betriebskostenabrechnungen, usw.) Hausmeisterservice, Winterdienst, Haustechnik, Büroservice, usw.</p>
      <p>Die K H D verfügt über die jeweils neuesten EDV-Programme und geschulte, langjährig erfahrene und motivierte Mitarbeiter.</p>
      <a class="more" href="#">+Read More</a>
    </div>
    <div class="van" role="img" aria-label="Photo of a white company van"></div>
    <div class="contact">
      <h2>KHD Büro- und Hausmeisterservice GmbH</h2>
      <div class="row"><svg width="14" height="10" viewBox="0 0 14 10"><rect x=".5" y=".5" width="13" height="9" fill="none" stroke="#2a8a25"/><path d="M.5.5 7 6 13.5.5" fill="none" stroke="#2a8a25"/></svg><span>Lindenplatz 14-16 in 27419 Drefling<br>vertreten durch Frau Helga Strelow,<br>Geschäftsführerin</span></div>
      <div class="row"><svg width="14" height="14" viewBox="0 0 14 14"><rect x="4" y="1" width="7" height="12" rx="1" fill="none" stroke="#2a8a25" stroke-width="1.5"/></svg><span>0 48 15/23 47 60</span></div>
      <div class="row"><svg width="14" height="14" viewBox="0 0 14 14"><rect x="1" y="5" width="12" height="7" fill="#2a8a25"/><rect x="3" y="1" width="8" height="4" fill="none" stroke="#2a8a25"/></svg><span>0 48 15/23 47 61</span></div>
      <div class="row"><svg width="14" height="14" viewBox="0 0 14 14"><circle cx="7" cy="7" r="6" fill="none" stroke="#2a8a25"/><ellipse cx="7" cy="7" rx="2.5" ry="6" fill="none" stroke="#2a8a25"/><path d="M1 7h12" stroke="#2a8a25"/></svg><span>info@kolvenhaus-drefling.de</span></div>
    </div>
  </section>
  <footer class="footer">
    <span>Copyright © 2014 KHD | All Rights Reserved.</span>
    <span><a href="#">Home</a> | <a href="#">About Us</a> | <a href="#">Contact Us</a></span>
  </footer>
</div>
</body>
</html>
```